Business card design with slight adjustment to current logo
Marlow Heating Cooling & Plumbing
Business card design with slight adjustment to current logo - Trade
Creative Brief
Bright & Fun-filled
no name wanted on card
no title wanted on card
3167 Penwick Ave Findlay, OH 45893
marlowhvacfindlay@examplemail.test
marlow-hvac.test
Heating Cooling Plumbing The logo I have is an older logo, we want to keep it the same but the type of file I have it flat looking, plain colored. If the logo can be tweaked to look brighter, less flat, but very similar so as not to look much different I would appreciate that. My hope was to have the flame in the logo look a little more like a flame, I think maybe the curve of it is just a little off, making it more like a shark fin or something. for the logo and business card, that color blue in logo is a favorite.
Tkvorel42 Tkvorel42
Cards can also say: Service & Install Free Estimates
This is more me looking for business card designs, if the logo can be adjusted a little bit and you have the idea for it, fine. But mainly I need good business card designs for current logo

```html
<!DOCTYPE html>
<html lang="en">
<head>
<meta charset="utf-8">
<title>Marlow Heating Cooling &amp; Plumbing – Business Card</title>
<link rel="stylesheet" href="https://fonts.googleapis.com/css2?family=Montserrat:wght@600;800&display=swap">
<style>
  :root {
    --card-bg: #ffffff;
    --ink: #2b2d33;
    --brand-blue: #2f86d0;
    --brand-blue-deep: #1f6fb8;
    --brand-blue-light: #cfe2f4;
  }
  html, body {
    margin: 0;
    padding: 0;
    width: 1200px;
    height: 742px;
    overflow: hidden;
    background: var(--card-bg);
  }
  .card {
    position: relative;
    width: 1200px;
    height: 742px;
    background: var(--card-bg);
    overflow: hidden;
  }
  .card__wave {
    position: absolute;
    left: 0;
    bottom: 0;
    width: 1200px;
    height: 742px;
  }
  .brand {
    position: absolute;
    left: 0;
    right: 0;
    top: 270px;
    text-align: center;
  }
  .brand__name {
    margin: 0;
    font-family: "Montserrat", sans-serif;
    font-weight: 800;
    font-size: 138px;
    line-height: 1;
    letter-spacing: 2px;
    color: var(--ink);
  }
  .services {
    position: absolute;
    left: 0;
    right: 0;
    top: 466px;
    display: flex;
    justify-content: center;
    gap: 30px;
    margin: 0;
    padding: 0;
    list-style: none;
    font-family: "Montserrat", sans-serif;
    font-weight: 600;
    font-size: 36px;
    letter-spacing: 2px;
    color: var(--ink);
  }
  .services__item {
    display: flex;
    align-items: center;
    gap: 14px;
  }
  .services__item::before {
    content: "";
    width: 18px;
    height: 18px;
    border-radius: 50%;
    background: var(--ink);
  }
</style>
</head>
<body>
  <main class="card">
    <svg class="card__wave" viewBox="0 0 1200 742" aria-hidden="true">
      <defs>
        <linearGradient id="waveGradient" x1="0" y1="0" x2="1" y2="0">
          <stop offset="0" stop-color="#e3eef9"/>
          <stop offset="0.45" stop-color="#8fbbe5"/>
          <stop offset="1" stop-color="#1f6fb8"/>
        </linearGradient>
        <linearGradient id="waveSoft" x1="0" y1="0" x2="1" y2="0">
          <stop offset="0" stop-color="#ffffff" stop-opacity="0"/>
          <stop offset="1" stop-color="#5fa0dc" stop-opacity="0.55"/>
        </linearGradient>
      </defs>
      <path d="M0 650 C 350 610, 760 560, 1200 510 L1200 742 L0 742 Z" fill="url(#waveSoft)"/>
      <path d="M0 690 C 400 650, 800 600, 1200 560 L1200 742 L0 742 Z" fill="url(#waveGradient)"/>
      <path d="M200 742 C 550 690, 900 640, 1200 610 L1200 742 Z" fill="var(--brand-blue-deep)" opacity="0.55"/>
    </svg>

    <header class="brand">
      <h1 class="brand__name">MARLOW</h1>
    </header>

    <ul class="services">
      <li class="services__item">HEATING</li>
      <li class="services__item">COOLING</li>
      <li class="services__item">PLUMBING</li>
    </ul>
  </main>
</body>
</html>
```